Quorvia.app is a developing company for entrepreneurs who need legal services.

Our Company Slogan is : The Only Law You Need
Company Info:
Quorvia is built to help anyone sort through the confusion of taking an idea from thoughts to a tangible reality, legally. We are here to help make the incorporation, idea protection and any other legal necessities an after thought for you. If you know your idea is the next Zentrix we will help you make the right legal decisions from the start.
Subscription Model packages: 2.99, 4.99, 9.99 options in three separate boxes. Choose a monthly option and get started with your startups legal services. Start Now!
Follow us on Social: @quorvia.app
Website template look:
Build an app landing page for the company. Need a clean subscription based template with my updated logo and color scheme to create a landing page, team, and contact page. I want to be able to edit the copy. Very simple and clean using company colors.
Target Market(s)
Gen-Z or Millenial aged entrepreneurs starting a business for the first time.
Industry/Entity Type
Legal
Coding
Coded - Design and coding required
Number of Pages Required
3 page
Font styles to use
Other font styles liked:
- Roboto, or Museo Sans 300,700
Look and feel

```html
<!DOCTYPE html>
<html lang="en">
<head>
<meta charset="utf-8">
<title>Quorvia — The Only Law You Need</title>
<link href="https://fonts.googleapis.com/css2?family=Raleway:wght@200;300;400;500;600;700&display=swap" rel="stylesheet">
<style>
:root{
  --green:#3a833b;
  --cyan:#22e0f0;
  --teal:#2fbfae;
  --lime:#9ccf52;
  --grey-bg:#ebebeb;
  --ink:#333;
  --muted:#666;
  --line:#4a86b8;
  --blue:#3498d6;
  --button-blue:#4d9cf5;
  --white:#fff;
}
*{box-sizing:border-box;margin:0;padding:0}
html,body{width:1200px;height:3000px;overflow:hidden}
body{font-family:"Raleway",sans-serif;color:var(--ink);background:var(--white)}
section{position:relative;width:1200px;overflow:hidden}
.abs{position:absolute}
.gradient{background:linear-gradient(90deg,var(--green) 0%,var(--teal) 50%,var(--cyan) 100%)}
.section-title{position:absolute;left:0;width:100%;text-align:center;font-weight:200;font-size:32px;letter-spacing:1px;text-transform:uppercase}
.divider{position:absolute;left:599px;width:1px;height:40px;background:var(--line)}
.divider-mark{position:absolute;left:594px;width:11px;height:11px;border:1px solid var(--line);border-radius:50%}

/* hero */
.hero{height:466px}
.brand{left:101px;top:40px;display:flex;align-items:center;gap:10px}
.brand-dot{width:26px;height:26px;border-radius:50%;background:var(--white)}
.brand-name{font-weight:700;font-size:20px;color:var(--white);letter-spacing:1px}
.menu{left:1064px;top:75px;width:30px}
.menu span{display:block;height:4px;background:var(--white);margin-bottom:5px;border-radius:1px}
.device-art{left:93px;top:178px;width:494px;height:240px;border-radius:30px;background:linear-gradient(160deg,rgba(255,255,255,.85),rgba(230,235,235,.6));transform:rotate(18deg) skewX(-20deg) scale(.85)}
.hero-title{left:614px;top:190px;color:var(--white);font-size:31px;line-height:34px}
.hero-title b{font-weight:400;display:block}
.hero-title span{font-weight:200;display:block}
.hero-copy{left:614px;top:276px;width:490px;color:var(--white);font-size:13px;line-height:23px}

/* provide */
.provide{height:386px;background:var(--grey-bg)}
.provide .section-title{top:64px;color:#555}
.provide .divider{top:118px}.provide .divider-mark{top:154px}
.features{left:87px;top:196px;width:1040px;display:flex}
.feature{width:346px;text-align:center;padding:0 8px;height:150px}
.feature + .feature{border-left:1px solid var(--line)}
.feature-icon{width:44px;height:44px;margin:10px auto 0;border:2px solid #c5dca2;border-radius:50%;display:flex;align-items:center;justify-content:center}
.feature h3{margin-top:30px;font-weight:500;font-size:18px;letter-spacing:.5px;color:#222}
.feature p{font-size:12.5px;line-height:17px;color:#444;margin-top:4px}

/* team */
.team{height:648px;background:var(--white)}
.team .section-title{top:64px;color:#555}
.team .divider{top:118px}.team .divider-mark{top:154px}
.member{width:178px;text-align:center}
.portrait{width:178px;height:142px;background:linear-gradient(160deg,#dfe6ec,#8a7a6e 55%,#3b4a66)}
.member h4{margin-top:14px;font-weight:500;font-size:18px;color:#222}
.member p{font-size:12.5px;color:#444;margin-top:6px}

/* subscribe */
.subscribe{height:630px}
.subscribe .section-title{top:64px;color:var(--white)}
.subscribe .divider{top:118px;background:rgba(255,255,255,.3)}
.subscribe .divider-mark{top:154px;border-color:#2a6d6a}
.plan{background:var(--white);text-align:center;width:194px}
.plan-name{margin:12px;height:62px;display:flex;align-items:center;justify-content:center;font-size:18px;color:#444;border-bottom:1px solid #eee}
.plan-name.boxed{background:#ececec;border:none;color:#777}
.plan-name.featured{background:var(--lime);border:2px dashed var(--button-blue);color:#4aa8e0}
.price{font-weight:700;font-size:34px;color:#333;margin-top:16px}
.per{font-size:11px;color:#bbb;margin-top:-4px}
.plan ul{list-style:none;margin-top:22px;font-size:11.5px;line-height:21.5px;color:#444}
.plan li.off{color:#ccc;text-decoration:line-through}
.plan-btn{margin:12px 12px 0;height:64px;background:#ececec;display:flex;align-items:center;justify-content:center;font-size:18px;color:#555}
.plan-btn.featured{background:var(--lime);border:2px dashed var(--button-blue);color:#4aa8e0}
.badge{right:-20px;top:50px;width:64px;height:64px;border-radius:50%;background:var(--white);border:2px solid var(--lime);display:flex;flex-direction:column;align-items:center;justify-content:center;color:#3a9ae0;font-size:8px;font-weight:700;line-height:8px}

/* contact */
.contact{height:654px;background:var(--grey-bg)}
.info{display:flex;gap:22px}
.info h5{font-weight:500;font-size:18px;color:#222}
.info p{font-size:11.5px;line-height:16px;color:#333;margin-top:4px}
.info a{color:var(--blue);text-decoration:none}
.touch-title{left:95px;top:244px;font-size:18px;font-weight:500;color:#222}
.field{height:24px;background:var(--white);border:1px solid #ccc;font-size:11px;color:#999;padding:4px 10px}
.send{left:91px;top:488px;width:152px;height:34px;background:var(--button-blue);color:var(--white);font-size:10px;font-weight:700;display:flex;align-items:center;justify-content:center}

/* social */
.social{height:216px;background:var(--blue);text-align:center;color:var(--white)}
.social h2{position:absolute;top:40px;width:100%;font-weight:200;font-size:30px;letter-spacing:14px}
.social-icons{left:0;top:98px;width:100%;display:flex;justify-content:center;gap:30px}
.social-icons span{width:22px;height:22px;border-radius:50%;background:var(--white)}
.social hr{position:absolute;left:95px;top:158px;width:1015px;border:none;border-top:1px solid rgba(255,255,255,.35)}
.copyright{top:190px;width:100%;font-size:10.5px}
</style>
</head>
<body>

<section class="hero gradient">
  <div class="abs brand"><span class="brand-dot"></span><span class="brand-name">QUORVIA</span></div>
  <div class="abs menu" aria-label="Menu"><span></span><span></span><span></span></div>
  <div class="abs device-art" role="img" aria-label="White smartphone lying at an angle showing the Quorvia app splash screen"></div>
  <h1 class="abs hero-title"><b>WHAT IS</b><span>QUORVIA</span></h1>
  <p class="abs hero-copy">Value Proposition: Mobile application that allows you to incorporate set up legal structure, and use basic templates to get off the ground taking your idea to real business. All encompassing platform to establish yourself legally and form a corporation that can stand the test of time.</p>
</section>

<section class="provide">
  <h2 class="section-title">What we provide...</h2>
  <div class="divider"></div><div class="divider-mark"></div>
  <div class="abs features">
    <div class="feature">
      <div class="feature-icon"><svg width="14" height="14" viewBox="0 0 14 14"><path d="M13 1 1 6l5 2 2 5z" fill="#777"/></svg></div>
      <h3>LEGAL STRUCTURE</h3>
      <p>Decide which way you want to incorporate</p>
    </div>
    <div class="feature">
      <div class="feature-icon" style="font-size:11px;color:#777">$</div>
      <h3>KEY DOCUMENTS</h3>
      <p>Basic NDA, SOW and Other important document template you can create.</p>
    </div>
    <div class="feature">
      <div class="feature-icon"><svg width="14" height="14" viewBox="0 0 14 14"><circle cx="5" cy="8" r="3" fill="none" stroke="#777" stroke-width="2"/><circle cx="10" cy="4" r="2" fill="none" stroke="#777" stroke-width="1.5"/></svg></div>
      <h3>CONNECTIONS</h3>
      <p>Algorithm connects you with right lower to move forward</p>
    </div>
  </div>
</section>

<section class="team">
  <h2 class="section-title">Our Team</h2>
  <div class="divider"></div><div class="divider-mark"></div>
  <div class="abs member" style="left:313px;top:196px"><div class="portrait" role="img" aria-label="Portrait photo of Mara"></div><h4>Mara</h4><p>Leagel adwiser</p></div>
  <div class="abs member" style="left:513px;top:196px"><div class="portrait" role="img" aria-label="Portrait photo of Dario"></div><h4>Dario</h4><p>Director</p></div>
  <div class="abs member" style="left:713px;top:196px"><div class="portrait" role="img" aria-label="Portrait photo of Lena"></div><h4>Lena</h4><p>Manager</p></div>
  <div class="abs member" style="left:313px;top:403px"><div class="portrait" role="img" aria-label="Portrait photo of Mara"></div><h4>Mara</h4><p>Leagel adwiser</p></div>
  <div class="abs member" style="left:513px;top:403px"><div class="portrait" role="img" aria-label="Portrait photo of Dario"></div><h4>Dario</h4><p>Director</p></div>
  <div class="abs member" style="left:713px;top:403px"><div class="portrait" role="img" aria-label="Portrait photo of Lena"></div><h4>Lena</h4><p>Manager</p></div>
</section>

<section class="subscribe gradient">
  <h2 class="section-title">Subscrbe</h2>
  <div class="divider"></div><div class="divider-mark"></div>
  <div class="abs plan" style="left:304px;top:196px;height:365px">
    <div class="plan-name">Silver</div>
    <div class="price">$2.99</div><div class="per">per month</div>
    <ul><li>Lorum Ipsum 1</li><li>Lorum Ipsum 2</li><li class="off">Lorum Ipsum 3</li><li class="off">Lorum Ipsum 4</li><li class="off">Lorum Ipsum 5</li></ul>
    <div class="plan-btn">Subscribe</div>
  </div>
  <div class="abs plan" style="left:523px;top:196px;height:375px">
    <div class="plan-name featured">Plattinum</div>
    <div class="abs badge"><svg width="18" height="18" viewBox="0 0 20 20"><path d="M10 1l2.6 6 6.4.5-4.9 4.2 1.5 6.3L10 14.6 4.4 18l1.5-6.3L1 7.5 7.4 7z" fill="none" stroke="#3a9ae0" stroke-width="1.5"/></svg>BEST<br>VALUE !</div>
    <div class="price">$9.99</div><div class="per">per month</div>
    <ul><li>Lorum Ipsum 1</li><li>Lorum Ipsum 2</li><li>Lorum Ipsum 3</li><li>Lorum Ipsum 4</li><li>Lorum Ipsum 5</li></ul>
    <div class="plan-btn featured">Subscribe</div>
  </div>
  <div class="abs plan" style="left:741px;top:196px;height:365px">
    <div class="plan-name boxed">Gold</div>
    <div class="price">$4.99</div><div class="per">per month</div>
    <ul><li>Lorum Ipsum 1</li><li>Lorum Ipsum 2</li><li>Lorum Ipsum 3</li><li class="off">Lorum Ipsum 4</li><li class="off">Lorum Ipsum 5</li></ul>
    <div class="plan-btn" style="margin-top:22px">Subscribe</div>
  </div>
</section>

<section class="contact">
  <div class="abs info" style="left:108px;top:76px">
    <svg width="22" height="30" viewBox="0 0 22 30" style="margin-top:12px"><path d="M11 1C5 1 1 5.5 1 11c0 7 10 18 10 18s10-11 10-18C21 5.5 17 1 11 1z" fill="var(--lime)"/><circle cx="11" cy="11" r="4" fill="var(--grey-bg)"/></svg>
    <div><h5>Address</h5><p>Building Name, 353<br>Street name, State, Contry</p></div>
  </div>
  <div class="abs info" style="left:454px;top:76px">
    <svg width="30" height="26" viewBox="0 0 24 24" style="margin-top:12px"><path d="M6.6 10.8a15 15 0 0 0 6.6 6.6l2.2-2.2c.3-.3.7-.4 1-.2 1.1.4 2.3.6 3.6.6.6 0 1 .4 1 1V20c0 .6-.4 1-1 1A17 17 0 0 1 3 4c0-.6.4-1 1-1h3.5c.6 0 1 .4 1 1 0 1.3.2 2.5.6 3.6.1.3 0 .7-.2 1z" fill="var(--lime)"/></svg>
    <div><h5>Phone</h5><p>1-234-5678-900</p></div>
  </div>
  <div class="abs info" style="left:800px;top:76px">
    <svg width="36" height="26" viewBox="0 0 36 26" style="margin-top:12px"><rect width="36" height="26" rx="2" fill="var(--lime)"/><path d="M1 2l17 13L35 2" fill="none" stroke="var(--grey-bg)" stroke-width="2"/></svg>
    <div><h5>Email</h5><p><a>mail@quorvia.app</a></p></div>
  </div>
  <h3 class="abs touch-title">Get in Touch</h3>
  <div class="abs field" style="left:95px;top:272px;width:320px">First Name</div>
  <div class="abs field" style="left:441px;top:272px;width:320px">Email address</div>
  <div class="abs field" style="left:788px;top:272px;width:320px">Your website</div>
  <div class="abs field" style="left:92px;top:308px;width:1022px;height:165px">Write message</div>
  <div class="abs send">SEND MESSAGE</div>
</section>

<section class="social">
  <h2>WE ARE SOCIAL</h2>
  <div class="abs social-icons" aria-label="Social links for @quorvia.app"><span></span><span></span><span></span></div>
  <hr>
  <p class="abs copyright">©2020 @ Quorvia. All Rights Reserved</p>
</section>

</body>
</html>
```